New Flyer Design Project

We need a flyer for our upcoming Rising Builders Summit.

5th Annual Rising Builders Summit
by the Bureau for Advancement in Public Works (B-AdPW)
Theme: Stand Tall
Date: January 24, 2020
Location: Harborview Lodge Hotel and Conference Center, San Marcos, TX
#StandTall

This is event is put together by B-AdPW's Rising Builders Ring of Merit. I have a logo for the Ring of Merit, but not something that indicates it's the Rising Builders Ring.

More about the Forum (please don't include on the flyer): This Forum provides a venue to openly discuss issues affecting women in our industry and ideas and strategies to address those issues.

Architecture, Construction and Engineering are all struggling with a tremendous shortage of skilled talent. It is more important than ever for organizations to be able to attract, support and retain a talented workforce and to encourage more women to pursue and build vibrant careers in architecture, engineering and construction. Unfortunately, their attrition rate also remains high in these industries. Developing and retaining a skilled workforce includes identifying and addressing the specific needs of women in our industry. Man or Woman; Male or Female Brain, B-AdPW’s Rising Builders Summit will give you and your team the tools you need to excel as an Employer of Choice and a roadmap for individual continued career planning and success .

This unique Forum provides a venue to engage everyone from executives to those just beginning their careers with active, hands-on sessions and vibrant networking with the best and brightest in the A/E/C industry. In our usual B-AdPW Forum style, Keynotes become table participants and table participants become presenters, encouraging participants to assimilate what they are learning. Join local, state and national leaders and subject matter experts as we candidly explore and address the issues affecting women in our industry .

```html
<!DOCTYPE html>
<html lang="en">
<head>
<meta charset="utf-8">
<title>Save the Date – 5th Annual Rising Builders Summit</title>
<link href="https://fonts.googleapis.com/css2?family=Signika:wght@400;600;700&display=swap" rel="stylesheet">
<style>
  :root {
    --brand-blue: #1f3f99;
    --band-blue-deep: #1d3a8f;
    --band-blue-light: #3c5cb0;
    --brand-green: #86b03a;
    --ink-grey: #555659;
    --arc-grey: #55565a;
    --sky-light: #d9eff4;
    --sky-mid: #a9dbe4;
    --paper: #ffffff;
  }
  * { margin: 0; padding: 0; box-sizing: border-box; }
  html, body { width: 900px; height: 1200px; overflow: hidden; background: var(--paper); }
  body { font-family: "Signika", sans-serif; }

  .flyer { position: relative; width: 900px; height: 1200px; background: var(--paper); overflow: hidden; }

  .frame {
    position: absolute; left: 34px; top: 37px; right: 34px; bottom: 37px;
    border: 8px solid var(--brand-blue);
    z-index: 3; pointer-events: none;
  }

  .logo-row {
    position: absolute; top: 78px; left: 0; width: 900px; height: 96px;
    display: flex; align-items: center; justify-content: center; gap: 26px;
  }
  .logo-mark { display: flex; align-items: center; gap: 14px; }
  .logo-mark .dot { width: 72px; height: 72px; border-radius: 50%; background: var(--brand-blue); }
  .logo-mark .name { font-size: 58px; font-weight: 400; color: var(--ink-grey); line-height: 1; }
  .logo-divider { width: 3px; height: 88px; background: var(--ink-grey); }
  .logo-merit { display: flex; align-items: center; gap: 12px; }
  .logo-merit .dot { width: 44px; height: 44px; border-radius: 50%; background: var(--brand-green); }
  .logo-merit .name { font-size: 28px; font-weight: 400; color: var(--ink-grey); line-height: 1; }

  .hero-band { position: absolute; left: 0; top: 0; width: 900px; height: 540px; z-index: 1; }

  .hero-text { position: absolute; left: 0; top: 205px; width: 900px; text-align: center; z-index: 2; }
  .hero-title {
    color: var(--brand-green); font-weight: 700; text-transform: uppercase;
    font-size: 104px; line-height: 88px; letter-spacing: -1px;
  }
  .hero-rule { width: 330px; height: 3px; background: #c9d3ea; margin: 22px auto 14px; opacity: .8; }
  .hero-date { color: var(--paper); font-weight: 700; font-size: 42px; line-height: 46px; }

  .event-info { position: absolute; left: 0; top: 530px; width: 900px; text-align: center; }
  .event-edition { color: var(--brand-green); font-weight: 700; font-size: 54px; line-height: 60px; text-transform: uppercase; }
  .event-name { color: var(--brand-green); font-weight: 700; font-size: 36px; line-height: 44px; text-transform: uppercase; }
  .event-meta { margin-top: 14px; color: var(--brand-blue); font-weight: 700; font-size: 19px; line-height: 25px; text-transform: uppercase; }

  .growth-scene {
    position: absolute; left: 62px; top: 716px; width: 776px; height: 420px;
    background: linear-gradient(180deg, var(--sky-light) 0%, var(--sky-mid) 70%, #f4c24a 100%);
    border-radius: 2px;
  }
</style>
</head>
<body>
<main class="flyer">
  <div class="frame"></div>

  <header class="logo-row">
    <div class="logo-mark"><span class="dot"></span><span class="name">B-AdPW</span></div>
    <span class="logo-divider"></span>
    <div class="logo-merit"><span class="dot"></span><span class="name">Ring of Merit</span></div>
  </header>

  <svg class="hero-band" viewBox="0 0 900 540" role="img" aria-label="Blue-tinted photo of a person with arms raised over a city skyline">
    <defs>
      <linearGradient id="bandFill" x1="0" y1="0" x2="0" y2="1">
        <stop offset="0" stop-color="#2f4ea4"/>
        <stop offset="0.55" stop-color="#3c5cb0"/>
        <stop offset="1" stop-color="#1d3a8f"/>
      </linearGradient>
    </defs>
    <path d="M0,270 Q450,130 900,270 L900,330 Q450,690 0,330 Z" fill="url(#bandFill)"/>
    <path d="M0,270 Q450,130 900,270" fill="none" stroke="var(--arc-grey)" stroke-width="9"/>
  </svg>

  <section class="hero-text">
    <h1 class="hero-title">Save<br>The Date</h1>
    <div class="hero-rule"></div>
    <p class="hero-date">JANUARY 24<br>2020</p>
  </section>

  <section class="event-info">
    <h2 class="event-edition">5th Annual</h2>
    <h3 class="event-name">Rising Builders Summit</h3>
    <p class="event-meta">By the Bureau for Advancement in Public Works<br>Harborview Lodge Hotel and Conference Center, San Marcos, TX</p>
  </section>

  <div class="growth-scene" role="img" aria-label="Illustration of a woman watering a growing plant beside stacks of gold coins and money bags in front of a pale blue city skyline"></div>
</main>
</body>
</html>
```